Seasoned logs and kindling for sale

producing firewood from beech,ash,oak and silver birch,
Kindling is produce from a variety of seasoned softwoods

Industry/Entity Type

Firewood

Contact Information for Business Card

mark Pellew 07812603948
dave Tillard 07846217035
e-mail,markp318@mailbrook.net

```html
<!DOCTYPE html>
<html lang="en">
<head>
<meta charset="utf-8">
<title>Firewood – Business Card</title>
<link rel="stylesheet" href="https://fonts.googleapis.com/css2?family=Josefin+Sans:wght@400&family=Open+Sans:wght@400&display=swap">
<style>
  :root {
    --forest: #43592a;
    --ink: #111111;
    --paper: #ffffff;
  }
  html, body {
    margin: 0;
    padding: 0;
    overflow: hidden;
    background: var(--paper);
  }
  .card {
    position: relative;
    width: 1200px;
    height: 833px;
    background: var(--paper);
    overflow: hidden;
  }
  .brand-name {
    position: absolute;
    left: 0;
    top: 180px;
    width: 1200px;
    margin: 0;
    text-align: center;
    font-family: "Josefin Sans", sans-serif;
    font-weight: 400;
    font-size: 64px;
    line-height: 70px;
    letter-spacing: 6px;
    text-transform: uppercase;
    color: var(--ink);
  }
  .tree-illustration {
    position: absolute;
    left: 452px;
    top: 272px;
    width: 290px;
    height: 326px;
    border-radius: 46% 46% 8% 8% / 40% 40% 8% 8%;
    background: radial-gradient(ellipse at 50% 32%, #4f6b33 0%, var(--forest) 55%, #8a8a80 82%, #e9e9e4 100%);
  }
  .contact {
    position: absolute;
    top: 388px;
    width: 280px;
    text-align: center;
  }
  .contact--left { left: 115px; }
  .contact--right { left: 800px; }
  .contact__name {
    font-family: "Josefin Sans", sans-serif;
    font-size: 32px;
    text-transform: capitalize;
    color: var(--ink);
    margin: 0;
    line-height: 40px;
  }
  .contact__rule {
    display: block;
    width: 280px;
    height: 6px;
    margin-top: 4px;
  }
  .contact__phone {
    display: flex;
    align-items: center;
    justify-content: center;
    gap: 10px;
    margin-top: 14px;
    font-family: "Josefin Sans", sans-serif;
    font-size: 21px;
    letter-spacing: 1px;
    color: var(--ink);
  }
  .contact__phone svg { width: 24px; height: 24px; }
  .email-band {
    position: absolute;
    left: 62px;
    top: 648px;
    width: 1074px;
    height: 34px;
    background: var(--forest);
    display: flex;
    align-items: center;
    justify-content: center;
    gap: 8px;
    font-family: "Open Sans", sans-serif;
    font-size: 21px;
    color: var(--paper);
  }
  .email-band svg { width: 28px; height: 20px; }
</style>
</head>
<body>
<main class="card">
  <h1 class="brand-name">Firewood</h1>

  <div class="tree-illustration" role="img" aria-label="Ink-and-green illustration of an oak tree above a stacked log pile and a wooden ladder"></div>

  <section class="contact contact--left">
    <p class="contact__name">mark Pellew</p>
    <svg class="contact__rule" viewBox="0 0 280 6" aria-hidden="true"><path d="M0 3 Q140 -2 280 3 Q140 8 0 3Z" fill="var(--forest)"/></svg>
    <div class="contact__phone">
      <svg viewBox="0 0 24 24" aria-hidden="true"><path d="M6.5 2.5 9.5 6.5 7.5 9c1.3 2.8 3.4 5 6.2 6.4l2.4-2 4 3-1.6 3.8C11 20 4 13 2.8 4.2Z" fill="var(--ink)"/><path d="M14 3a7 7 0 0 1 7 7M14 6.5a3.5 3.5 0 0 1 3.5 3.5" stroke="var(--ink)" stroke-width="1.6" fill="none"/></svg>
      <span>07812603948</span>
    </div>
  </section>

  <section class="contact contact--right">
    <p class="contact__name">dave Tillard</p>
    <svg class="contact__rule" viewBox="0 0 280 6" aria-hidden="true"><path d="M0 3 Q140 -2 280 3 Q140 8 0 3Z" fill="var(--forest)"/></svg>
    <div class="contact__phone">
      <svg viewBox="0 0 24 24" aria-hidden="true"><path d="M6.5 2.5 9.5 6.5 7.5 9c1.3 2.8 3.4 5 6.2 6.4l2.4-2 4 3-1.6 3.8C11 20 4 13 2.8 4.2Z" fill="var(--ink)"/><path d="M14 3a7 7 0 0 1 7 7M14 6.5a3.5 3.5 0 0 1 3.5 3.5" stroke="var(--ink)" stroke-width="1.6" fill="none"/></svg>
      <span>07846217035</span>
    </div>
  </section>

  <footer class="email-band">
    <svg viewBox="0 0 28 20" aria-hidden="true"><path d="M1 8 14 1l13 7v11H1Z" fill="var(--paper)"/><path d="M1 8l13 7 13-7" stroke="var(--forest)" stroke-width="1.4" fill="none"/></svg>
    <span>: markp318@mailbrook.net</span>
  </footer>
</main>
</body>
</html>
```